Data Analytics Irish company needs Stationery Design

We need a stationery design for our data analytics company based in Dublin called 'Numbryx': we develop innovative web-based corporate applications exploiting advanced Machine Learning and Data Mining techniques.
Like the animal that inspired our company name, the final design should communicate intelligence and passion; on the other hand, we want to keep the highest professional appeal.
We love our current logo and we have tried out several color variations: we prefer solutions (see the logo attached) with white design and dark backgrounds, but we will also be glad to see some designs that follow the colors of the palette of the attached web screenshot.

```html
<!DOCTYPE html>
<html lang="en">
<head>
<meta charset="utf-8">
<title>Numbryx – Business Card</title>
<link rel="stylesheet" href="https://fonts.googleapis.com/css2?family=Questrial&family=Montserrat:wght@600&display=swap">
<style>
  :root {
    --backdrop: #2b2b2b;
    --card-dark: #222222;
    --card-dark-edge: #1a1a1a;
    --card-light: #f4f4f4;
    --brand-blue: #2f6db5;
    --ink-grey: #4a4a4a;
    --text-light: #d6d6d6;
    --text-muted: #a8a8a8;
  }
  * { margin: 0; padding: 0; box-sizing: border-box; }
  html, body { width: 1200px; height: 900px; overflow: hidden; }
  body {
    background: var(--backdrop);
    font-family: "Questrial", sans-serif;
    position: relative;
  }
  .card {
    position: absolute;
    left: 300px;
    width: 600px;
    height: 343px;
    border-radius: 4px;
    overflow: hidden;
    box-shadow: 0 14px 30px rgba(0,0,0,.45);
  }
  .card-back {
    top: 70px;
    background: radial-gradient(circle at 50% 50%, #2c2c2c 0%, var(--card-dark) 60%, var(--card-dark-edge) 100%);
    display: flex;
    align-items: center;
    justify-content: center;
  }
  .card-front { top: 487px; background: var(--card-dark); }
  .card-front svg.card-art { position: absolute; inset: 0; }

  .wordmark {
    display: flex;
    align-items: center;
    gap: 14px;
  }
  .wordmark-dot {
    width: 54px; height: 54px;
    border-radius: 50%;
    background: var(--brand-blue);
  }
  .wordmark-name {
    font-family: "Questrial", sans-serif;
    font-size: 58px;
    letter-spacing: 1px;
    line-height: 1;
  }
  .card-back .wordmark-name { color: var(--text-light); }
  .card-front .wordmark { position: absolute; left: 70px; top: 62px; }
  .card-front .wordmark-dot { width: 48px; height: 48px; }
  .card-front .wordmark-name { color: var(--ink-grey); font-size: 52px; }

  .holder {
    position: absolute;
    right: 32px;
    top: 236px;
    text-align: right;
  }
  .holder-name {
    font-family: "Montserrat", sans-serif;
    font-weight: 600;
    font-size: 20px;
    line-height: 24px;
    letter-spacing: 1px;
    color: var(--text-light);
  }
  .holder-title {
    font-size: 14px;
    line-height: 18px;
    color: var(--text-muted);
    margin-top: 2px;
  }
  .contact-list {
    position: absolute;
    left: 70px;
    bottom: 18px;
    list-style: none;
  }
  .contact-list li {
    display: flex;
    align-items: center;
    gap: 8px;
    font-size: 15px;
    color: var(--text-muted);
    line-height: 24px;
  }
  .contact-list svg { width: 15px; height: 15px; }
</style>
</head>
<body>

  <section class="card card-back" aria-label="Business card back">
    <div class="wordmark">
      <span class="wordmark-dot"></span>
      <span class="wordmark-name">numbryx</span>
    </div>
  </section>

  <section class="card card-front" aria-label="Business card front">
    <svg class="card-art" viewBox="0 0 600 343" width="600" height="343" aria-hidden="true">
      <defs>
        <linearGradient id="rule-fade" x1="0" y1="0" x2="1" y2="0">
          <stop offset="0" stop-color="#2f6db5" stop-opacity="0"/>
          <stop offset="0.35" stop-color="#2f6db5" stop-opacity="0.8"/>
          <stop offset="1" stop-color="#2f6db5"/>
        </linearGradient>
      </defs>
      <path d="M0 0 H600 V118 C440 170 300 222 150 240 C100 245 50 246 0 246 Z" fill="#f4f4f4"/>
      <path d="M150 240 C300 222 440 170 600 118" fill="none" stroke="url(#rule-fade)" stroke-width="4"/>
      <path d="M524 141 L540 135 L535 150 Z" fill="#2f6db5"/>
    </svg>

    <div class="wordmark">
      <span class="wordmark-dot"></span>
      <span class="wordmark-name">numbryx</span>
    </div>

    <div class="holder">
      <p class="holder-name">CIARA BRENNAN</p>
      <p class="holder-title">Managing Director</p>
    </div>

    <ul class="contact-list">
      <li>
        <svg viewBox="0 0 16 16"><rect x="4" y="1" width="8" height="14" rx="1.5" fill="none" stroke="#2f6db5" stroke-width="1.6"/><circle cx="8" cy="12.5" r="0.9" fill="#2f6db5"/></svg>
        01-555-0187
      </li>
      <li>
        <svg viewBox="0 0 16 16"><rect x="1.5" y="3.5" width="13" height="9" rx="1" fill="none" stroke="#2f6db5" stroke-width="1.6"/><path d="M2 4 L8 9 L14 4" fill="none" stroke="#2f6db5" stroke-width="1.4"/></svg>
        info@numbryx.com
      </li>
      <li>
        <svg viewBox="0 0 16 16"><circle cx="8" cy="8" r="6.5" fill="none" stroke="#2f6db5" stroke-width="1.5"/><ellipse cx="8" cy="8" rx="2.8" ry="6.5" fill="none" stroke="#2f6db5" stroke-width="1.2"/><path d="M1.5 8 H14.5" stroke="#2f6db5" stroke-width="1.2"/></svg>
        www.numbryx.com
      </li>
    </ul>
  </section>

</body>
</html>
```